Quick Tray Packs

Need a very simple diagonal random design on bag. using 2 colors only
Packaging material on a roll. 11' Wide total, do not need eye spot since it is random print.
Target Market(s)
hospitality industry
Colors
Designer to choose colors to be used in the design.
Requirements
Must have
- Open for design ideas very simple since it is repeat.the text should be diagonal.
- Need for whole bag to be black, the test can be in Gold.
- On the front of the bag:
- Velvet Crest Coffee
- 100% Arabica Coffee
- Back of the bag:
- This package contains one filter pack coffee and may
- also contain sugar, non-dairy creamer, sugar sub., and stirrer.
- Corvane & Reed Coffee
- Alder Bay, TX 75999

```html
<!DOCTYPE html>
<html lang="en">
<head>
<meta charset="utf-8">
<title>Quick Tray Packs – Velvet Crest Coffee Bag Print</title>
<link rel="stylesheet" href="https://fonts.googleapis.com/css2?family=Libre+Caslon+Text:wght@400;700&family=Playfair+Display:wght@600&display=swap">
<style>
  :root {
    --bag-black: #000000;
    --gold: #cda34f;
    --edge: #2c3b3b;
  }
  html, body {
    margin: 0;
    padding: 0;
    width: 1200px;
    height: 638px;
    overflow: hidden;
    background: var(--bag-black);
  }
  .bag-print {
    display: block;
    width: 1200px;
    height: 638px;
    box-sizing: border-box;
    border: 1px solid var(--edge);
    background: var(--bag-black);
  }
  .brand-name {
    font-family: "Playfair Display", Georgia, serif;
    font-weight: 600;
    fill: var(--gold);
  }
  .blend-name {
    font-family: "Libre Caslon Text", Georgia, serif;
    font-weight: 400;
    font-size: 25px;
    fill: var(--bag-black);
  }
  .blend-origin {
    font-family: "Libre Caslon Text", Georgia, serif;
    font-weight: 700;
    font-size: 11px;
    letter-spacing: 1px;
    fill: var(--bag-black);
  }
  .blend-divider {
    stroke: var(--bag-black);
    stroke-width: 2.5;
    stroke-dasharray: 9 5;
  }
  .roast-label {
    font-family: "Libre Caslon Text", Georgia, serif;
    font-size: 25px;
    fill: var(--gold);
  }
  .maker-address {
    font-family: "Libre Caslon Text", Georgia, serif;
    font-weight: 700;
    font-size: 13px;
    fill: var(--gold);
  }
  .contents-note {
    font-family: "Libre Caslon Text", Georgia, serif;
    font-size: 12.5px;
    fill: var(--gold);
  }
</style>
</head>
<body>
<svg class="bag-print" viewBox="0 0 1200 638" xmlns="http://www.w3.org/2000/svg" aria-label="Velvet Crest Coffee bag print">
  <g class="brand-lockup" transform="translate(612 250) rotate(-17)">
    <text class="brand-name" x="-30" y="-40" font-size="52" text-anchor="middle">Café</text>
    <text class="brand-name" x="0" y="40" font-size="86" text-anchor="middle" letter-spacing="4">SOLENNE</text>
  </g>

  <polygon class="blend-band" points="328,461 696,346 719,416 328,541" fill="var(--gold)"/>

  <g class="blend-panel" transform="translate(536 430) rotate(-17.5)">
    <text class="blend-name" x="0" y="0" text-anchor="middle">VELVET CREST</text>
    <line class="blend-divider" x1="-104" y1="12" x2="106" y2="12"/>
    <text class="blend-origin" x="-4" y="29" text-anchor="middle">100% ARABICA COFFEE</text>
    <text class="roast-label" x="-55" y="76" text-anchor="middle">REGULAR</text>
  </g>

  <g class="maker-info" transform="translate(216 354) rotate(-17)">
    <text class="maker-address" x="0" y="0" text-anchor="middle">Corvane &amp; Reed Coffee</text>
    <text class="maker-address" x="0" y="18" text-anchor="middle">Alder Bay, TX 75999</text>
  </g>

  <g class="contents-info" transform="translate(990 312) rotate(-17)">
    <text class="contents-note" x="0" y="-24" text-anchor="middle">This package contains one</text>
    <text class="contents-note" x="0" y="-6" text-anchor="middle">filter pack coffee and may</text>
    <text class="contents-note" x="0" y="12" text-anchor="middle">also contain sugar, non-dairy</text>
    <text class="contents-note" x="0" y="30" text-anchor="middle">creams, sugar sub and stirrer</text>
  </g>
</svg>
</body>
</html>
```